Country House in Italy Needs a Business Card Design

We need a business card design for “Casale del Ruscello”, a modern concept of a Farm Holidays/Country House to be opened in central Italy.
Attached is the company logo you did for us in the past.
Please
- create a double-sided business card design
- on the back I would like to have the logo
- on the front the copy
Copy on card:
o Casale del Ruscello
o Address: Via Fontalba, 14
Cingoli (MC), Italy
o Website: www.casaledelruscello.it
o Email: info@casaledelruscello.it
o my name : Lucilla
o my mobile phone number: +39 347 8124591
In the distribution of information keep in mind the possible inclusion also of a landline telephone number (currently not available / existing).
WE WOULD LIKE TO HAVE A MODERN, PROFFESIONAL, OUT OF THE BOX BUSINESS CARD. BE AS CREATIVE AS YOU WOULD LIKE.

```html
<!DOCTYPE html>
<html lang="it">
<head>
<meta charset="utf-8">
<title>Casale del Ruscello – Business Card</title>
<link href="https://fonts.googleapis.com/css2?family=Cormorant+Garamond:wght@500&family=Lato:wght@400;700;900&display=swap" rel="stylesheet">
<style>
  :root {
    --stage: #2a2a2b;
    --gold-light: #a69068;
    --gold: #8f7a52;
    --gold-dark: #7a6642;
    --paper: #ffffff;
    --paper-shade: #eeeeee;
    --accent: #de6026;
    --ink: #1c1a17;
    --brown-text: #6e5a38;
    --cream: #f3ede2;
  }
  * { margin: 0; padding: 0; box-sizing: border-box; }
  html, body {
    width: 1200px; height: 900px; overflow: hidden;
    background: var(--stage);
  }
  .stage {
    position: relative; width: 1200px; height: 900px;
    display: flex; flex-direction: column; align-items: center; justify-content: center; gap: 40px;
  }
  .card {
    position: relative; width: 560px; height: 320px;
    border-radius: 16px; overflow: hidden;
    box-shadow: 0 14px 30px rgba(0,0,0,.45);
  }

  /* Back side */
  .card-back {
    background: linear-gradient(135deg, var(--gold-light), var(--gold) 55%, var(--gold-dark));
    display: flex; align-items: center; justify-content: center; gap: 18px;
  }
  .back-mark {
    width: 26px; height: 26px; border-radius: 50%;
    background: var(--cream);
  }
  .back-name {
    font-family: "Cormorant Garamond", serif; font-weight: 500;
    font-size: 46px; color: var(--cream); letter-spacing: .5px;
  }

  /* Front side */
  .card-front {
    background: linear-gradient(160deg, var(--paper) 60%, var(--paper-shade));
  }
  .front-band {
    position: absolute; left: 0; right: 0; bottom: 0; height: 74px;
    background: linear-gradient(90deg, var(--gold-dark), var(--gold-light));
    border-top: 5px solid var(--accent);
  }
  .divider {
    position: absolute; left: 292px; top: 40px; width: 3px; height: 180px;
    background: linear-gradient(180deg, rgba(143,122,82,0), var(--gold) 45%, rgba(143,122,82,0));
  }
  .brand-block {
    position: absolute; left: 24px; top: 70px; width: 258px;
    display: flex; flex-direction: column; align-items: center;
  }
  .brand-line { display: flex; align-items: center; gap: 8px; }
  .brand-mark { width: 14px; height: 14px; border-radius: 50%; background: var(--accent); flex: none; }
  .brand-name {
    font-family: "Cormorant Garamond", serif; font-weight: 500;
    font-size: 31px; color: var(--brown-text); white-space: nowrap;
  }
  .address {
    margin-top: 22px; text-align: center;
    font-family: "Lato", sans-serif; font-weight: 900; font-size: 15px; line-height: 1.4;
    color: var(--ink);
  }
  .contact-block {
    position: absolute; left: 318px; top: 36px; width: 230px;
    font-family: "Lato", sans-serif;
  }
  .person-name {
    font-weight: 900; font-size: 17px; letter-spacing: .5px;
    color: var(--brown-text); text-transform: uppercase;
  }
  .person-role { font-weight: 700; font-size: 12.5px; color: var(--ink); margin-bottom: 20px; }
  .contact-list { list-style: none; }
  .contact-item {
    display: flex; align-items: center; gap: 10px; margin-bottom: 9px;
    font-weight: 700; font-size: 13.5px; color: var(--brown-text); white-space: nowrap;
  }
  .contact-icon {
    width: 24px; height: 24px; border-radius: 50%; flex: none;
    background: var(--gold-dark);
    display: flex; align-items: center; justify-content: center;
  }
  .contact-icon svg { width: 14px; height: 14px; }
</style>
</head>
<body>
<main class="stage">

  <section class="card card-back" aria-label="Card back">
    <span class="back-mark"></span>
    <span class="back-name">Casale del Ruscello</span>
  </section>

  <section class="card card-front" aria-label="Card front">
    <div class="brand-block">
      <div class="brand-line">
        <span class="brand-mark"></span>
        <span class="brand-name">Casale del Ruscello</span>
      </div>
      <p class="address">Via/Località Fontalba, 14<br>06089 Valdirose (PG), Italy</p>
    </div>

    <div class="divider"></div>

    <div class="contact-block">
      <p class="person-name">Lucilla</p>
      <p class="person-role">Centre Director</p>
      <ul class="contact-list">
        <li class="contact-item">
          <span class="contact-icon">
            <svg viewBox="0 0 16 16" fill="#fff"><path d="M2 6c0-2 3-3 6-3s6 1 6 3v1h-3V5.5H5V7H2z"/><rect x="3.5" y="8" width="9" height="5" rx="1"/></svg>
          </span>+39 347 8124591
        </li>
        <li class="contact-item">
          <span class="contact-icon">
            <svg viewBox="0 0 16 16" fill="#fff"><path d="M4 2l2.2 3-1.3 1.4c.8 1.8 2.1 3.1 3.8 3.9L10 9l3 2.2-1.2 2.3C7 13.2 2.8 9 2.5 4.2z"/></svg>
          </span>(+39) 0742 518 346
        </li>
        <li class="contact-item">
          <span class="contact-icon">
            <svg viewBox="0 0 16 16"><rect x="2" y="4" width="12" height="8" fill="#fff"/><path d="M2 4l6 5 6-5" fill="none" stroke="#7a6642" stroke-width="1.2"/></svg>
          </span>info@casaledelruscello.it
        </li>
        <li class="contact-item">
          <span class="contact-icon">
            <svg viewBox="0 0 16 16" fill="none" stroke="#fff" stroke-width="1.8" stroke-linecap="round"><path d="M7 9.5l-1.8 1.8a2 2 0 01-2.8-2.8L4.5 6.5"/><path d="M9 6.5l1.8-1.8a2 2 0 012.8 2.8L11.5 9.5"/><path d="M6.3 9.7l3.4-3.4"/></svg>
          </span>www.casaledelruscello.it
        </li>
      </ul>
    </div>

    <div class="front-band"></div>
  </section>

</main>
</body>
</html>
```